Software company needs a great powerpoint template

We need a powerpoint template for our growing company. Our software helps hospitals achieve quality via automating tedius manual tasks, performing them better, faster and easier than a person can. See our logo below and check out our website at qvr-carewise.com for more ideas/informaton. We will use this template for sales presentations, trade show demonstrations and partnership proposals.

Target Market(s)

Hospital managers & directors

Industry/Entity Type

Hospital

Contact Information for Business Card

name, title, office telephone, cell phone, email and website

Font styles to use
Sans Serif

Colors
2f74b3
33b8a4

Requirements
Must have
• use blues and greens, san serif fonts
Nice to have
• modern feel yet still somewhat converative

```html
<!DOCTYPE html>
<html lang="en">
<head>
<meta charset="utf-8">
<title>Quiver Care Systems – Presentation Template</title>
<link href="https://fonts.googleapis.com/css2?family=Arimo:wght@400;700&display=swap" rel="stylesheet">
<style>
  :root {
    --navy: #2a5189;
    --blue: #2f74b3;
    --blue-light: #7fb0da;
    --green: #33b8a4;
    --green-dark: #258f80;
    --ink: #2b3440;
    --white: #ffffff;
    --paper: #f4f7fa;
    --frame: #c9d6e6;
    --gap: #ffffff;
  }
  * { box-sizing: border-box; margin: 0; padding: 0; }
  html, body { width: 1200px; height: 1018px; overflow: hidden; background: var(--gap); }
  .sheet { position: relative; width: 1200px; height: 1018px; font-family: "Arimo", sans-serif; }
  .slide { position: absolute; width: 595px; overflow: hidden; background: linear-gradient(180deg, #ffffff 0%, #eef3f7 100%); }
  .col-left { left: 0; } .col-right { left: 605px; }
  .row-1 { top: 0; height: 334px; }
  .row-2 { top: 342px; height: 330px; }
  .row-3 { top: 680px; height: 338px; }

  .photo { position: absolute; }
  .title-bar {
    position: absolute; left: 0; right: 0; top: 12px; height: 42px;
    background: linear-gradient(90deg, var(--navy) 0%, var(--blue) 55%, var(--blue-light) 82%, rgba(255,255,255,0) 100%);
    color: var(--white); font: 400 20px/42px "Arimo", sans-serif; padding-left: 30px;
  }
  .title-bar::after {
    content: ""; position: absolute; left: 0; bottom: -4px; width: 220px; height: 4px; background: var(--green);
  }

  /* title slide */
  .brand-band { position: absolute; left: 0; right: 0; top: 232px; height: 102px; background: rgba(255,255,255,.9); }
  .brand-mark { position: absolute; left: 150px; top: 30px; display: flex; align-items: center; gap: 9px;
    font: 700 36px/1 "Arimo", sans-serif; color: var(--blue); }
  .brand-mark .dot { width: 14px; height: 14px; background: var(--green); border-radius: 50%; }
  .brand-rule { position: absolute; left: 292px; top: 22px; width: 2px; height: 60px; background: var(--navy); }
  .brand-name { position: absolute; left: 308px; top: 26px; font: 400 21px/1.25 "Arimo", sans-serif; color: var(--navy); }

  /* agenda */
  .agenda { position: absolute; left: 50px; top: 78px; list-style: none; }
  .agenda li { display: flex; align-items: center; gap: 14px; height: 35.5px; font: 400 14px "Arimo", sans-serif; color: var(--ink); }
  .agenda svg { width: 25px; height: 25px; flex: none; }

  /* divider */
  .divider-band { position: absolute; right: 0; background: rgba(42,81,137,.94); color: var(--white);
    font: 400 24px/1.25 "Arimo", sans-serif; padding: 24px 0 0 36px; border-top: 4px solid var(--green); }
  .divider-band::before { content: ""; position: absolute; left: 18px; top: 18px; bottom: 18px; width: 2px; background: var(--green); }

  /* bullets */
  .bullet-box { position: absolute; left: 14px; top: 88px; width: 288px; height: 186px; background: var(--navy);
    padding: 20px 16px 0 24px; border: 2px solid var(--frame); border-left: 5px solid var(--green); }
  .bullet-box ul { list-style: disc; color: var(--white); font: 400 12px/1.45 "Arimo", sans-serif; padding-left: 12px; }
  .bullet-box li { margin-bottom: 12px; }
  .bullet-box li::marker { color: var(--green); }

  /* quote */
  .quote-hex { position: absolute; left: 48px; top: 118px; width: 410px; height: 160px; }
  .quote-text { position: absolute; left: 108px; top: 146px; width: 294px; color: var(--white);
    font: 400 12px/1.5 "Arimo", sans-serif; text-align: center; }
</style>
</head>
<body>
<main class="sheet">

  <section class="slide col-left row-1">
    <div class="photo" role="img" aria-label="Team of smiling hospital doctors in white coats and blue scrubs"
         style="inset:0;background:radial-gradient(ellipse at 30% 45%,#f6f8fa 0%,rgba(246,248,250,0) 40%),radial-gradient(ellipse at 70% 55%,#9cc0dc 0%,rgba(156,192,220,0) 45%),linear-gradient(180deg,#bcd7e8 0%,#e3edf4 50%,#a9c7dc 100%)"></div>
    <div class="brand-band">
      <div class="brand-mark"><span class="dot"></span>QVR</div>
      <div class="brand-rule"></div>
      <p class="brand-name">Quiver Care<br>Systems LLC</p>
    </div>
  </section>

  <section class="slide col-right row-1">
    <h2 class="title-bar">Agenda</h2>
    <ul class="agenda">
      <li><svg viewBox="0 0 26 26"><circle cx="13" cy="13" r="12" fill="var(--blue)"/><circle cx="11.5" cy="11.5" r="4.5" fill="none" stroke="#fff" stroke-width="2"/><path d="M15 15l4 4" stroke="#fff" stroke-width="2"/></svg>Subject</li>
      <li><svg viewBox="0 0 26 26"><circle cx="13" cy="13" r="12" fill="var(--green)"/><circle cx="13" cy="13" r="5" fill="#fff"/></svg>Subject</li>
      <li><svg viewBox="0 0 26 26"><circle cx="13" cy="13" r="12" fill="var(--blue)"/><path d="M13 6a5 5 0 0 0-5 5c0 4 5 9 5 9s5-5 5-9a5 5 0 0 0-5-5z" fill="#fff"/></svg>Subject</li>
      <li><svg viewBox="0 0 26 26"><circle cx="13" cy="13" r="12" fill="var(--green)"/><path d="M7 19V8M7 19h12M10 16v-4M13 16v-6M16 16v-3" stroke="#fff" stroke-width="2"/></svg>Subject</li>
      <li><svg viewBox="0 0 26 26"><circle cx="13" cy="13" r="12" fill="var(--blue)"/><path d="M8 13l3 3 7-7" fill="none" stroke="#fff" stroke-width="2.4"/></svg>Subject</li>
      <li><svg viewBox="0 0 26 26"><circle cx="13" cy="13" r="12" fill="var(--green)"/><rect x="8" y="8" width="10" height="10" fill="#fff"/></svg>Subject</li>
      <li><svg viewBox="0 0 26 26"><circle cx="13" cy="13" r="12" fill="var(--blue)"/><path d="M7 15a6 6 0 0 1 12 0v3H7z" fill="#fff"/></svg>Subject</li>
    </ul>
  </section>

  <section class="slide col-left row-2">
    <div class="photo" role="img" aria-label="Doctor and nurse discussing a case at a laptop"
         style="inset:0;background:radial-gradient(ellipse at 28% 40%,#f3efe9 0%,rgba(243,239,233,0) 45%),radial-gradient(ellipse at 55% 35%,#8fb6d3 0%,rgba(143,182,211,0) 40%),radial-gradient(ellipse at 75% 50%,#e9d6c4 0%,rgba(233,214,196,0) 40%),linear-gradient(110deg,#e2ddd6 0%,#cfd9e2 50%,#dfe4e8 100%)"></div>
    <div class="divider-band" style="left:270px;top:200px;height:108px">This Is a Subject<br>Divider Slide</div>
  </section>

  <section class="slide col-right row-2">
    <h2 class="title-bar">This Is A Bullet Point Slide</h2>
    <div class="bullet-box">
      <ul>
        <li>Lorem ipsum dolor sit amet, consectetuer adipiscing elit.</li>
        <li>Nunc viverra imperdiet enim. Fusce est. Vivamus a tellus.</li>
        <li>Pellentesque habitant morbi tristique senectus et netus et malesuada fames ac.</li>
      </ul>
    </div>
    <div class="photo" role="img" aria-label="Doctor holding a piggy bank with a stethoscope"
         style="left:314px;top:66px;width:269px;height:220px;border:2px solid var(--frame);background:radial-gradient(ellipse at 45% 60%,#f0c9c2 0%,rgba(240,201,194,0) 35%),radial-gradient(ellipse at 70% 30%,#dfe6ee 0%,rgba(223,230,238,0) 50%),linear-gradient(135deg,#ffffff 0%,#eef1f4 60%,#dfe5ea 100%)"></div>
  </section>

  <section class="slide col-left row-3">
    <h2 class="title-bar">This Is A Quote Slide</h2>
    <div class="photo" role="img" aria-label="Faded photo of medical staff reviewing records"
         style="left:240px;top:105px;width:355px;height:190px;background:linear-gradient(90deg,rgba(220,228,236,0) 0%,#d3dde6 35%,#bccbd8 100%)"></div>
    <svg class="quote-hex" viewBox="0 0 410 160" aria-hidden="true"><polygon points="40,0 370,0 410,80 370,160 40,160 0,80" fill="var(--navy)"/><polygon points="40,0 370,0 376,12 34,12" fill="var(--green)"/></svg>
    <p class="quote-text">“Lorem ipsum dolor sit amet, consectetuer adipiscing elit. Maecenas porttitor congue massa. Fusce posuere, magna sed pulvinar ultricies, purus lectus malesuada libero, sit amet commodo magna eros quis urna”</p>
  </section>

  <section class="slide col-right row-3">
    <div class="photo" role="img" aria-label="Surgeon in mask and cap in an operating room"
         style="inset:0;background:radial-gradient(ellipse at 25% 45%,#f2f4f5 0%,rgba(242,244,245,0) 30%),radial-gradient(ellipse at 22% 18%,#6f9fc7 0%,rgba(111,159,199,0) 30%),radial-gradient(ellipse at 85% 40%,#5fa6ad 0%,rgba(95,166,173,0) 35%),linear-gradient(90deg,#9cbfd2 0%,#cddde5 45%,#e4ebee 65%,#8fb6bf 100%)"></div>
    <div class="divider-band" style="left:228px;top:194px;height:114px;padding-top:28px">This Is a Subject<br>Divider Slide</div>
  </section>

</main>
</body>
</html>
```